Business Card Design

It's an investment advisory service for individuals with all there investment needs. Also financial consulting to businesses and governmental agencies on retirement plans etc. It's personalized not commoditized help. Should show strength, knowledge and money orientation.
Updates

Reason: Will be out of town setting up office.

Reason: waiting for the 2/3rds of group to vote

Reason: only half the votes are in, I'm calling and getting verbals, but at this time we are down to 2 designs.

Industry/Entity Type

Investment

Contact Information for Business Card

B. Rel K. Financial Consulting and Wealth Management, Desmond Wick Harlow, 5172 Paseo Loma Verde Crest, San Diego, CA 92131-4817, Registered Investment Advisor

Requirements
Nice to have
• Something money oriented

```html
<!DOCTYPE html>
<html lang="en">
<head>
<meta charset="utf-8">
<title>B. Rel K. Financial Consulting – Business Card</title>
<link rel="stylesheet" href="https://fonts.googleapis.com/css2?family=Poppins:wght@600;700&family=Lato:wght@400&display=swap">
<style>
  :root {
    --page-bg: #ece8e1;
    --card-gold-edge: #f2c21c;
    --card-gold-mid: #f7e35a;
    --card-light: #fbf6a6;
    --card-orange-edge: #f1b52a;
    --name-red: #e8202a;
    --company-green: #0fa14a;
    --body-ink: #222222;
    --coin-deep: #c98d12;
    --coin-light: #f6d766;
  }
  * { margin: 0; padding: 0; box-sizing: border-box; }
  html, body {
    width: 1200px;
    height: 900px;
    overflow: hidden;
    background: var(--page-bg);
  }
  .canvas {
    width: 1200px;
    height: 900px;
    display: flex;
    align-items: center;
    justify-content: center;
  }
  .business-card {
    position: relative;
    width: 1000px;
    height: 572px;
    background: linear-gradient(90deg,
      var(--card-gold-edge) 0%,
      var(--card-gold-mid) 18%,
      var(--card-light) 50%,
      var(--card-gold-mid) 82%,
      var(--card-orange-edge) 100%);
    box-shadow: 0 10px 30px rgba(0,0,0,0.18);
    overflow: hidden;
  }
  .advisor-name {
    position: absolute;
    top: 48px;
    right: 60px;
    font-family: 'Poppins', sans-serif;
    font-weight: 700;
    font-size: 42px;
    color: var(--name-red);
    letter-spacing: 0.5px;
  }
  .company-name {
    position: absolute;
    top: 128px;
    left: 250px;
    font-family: 'Poppins', sans-serif;
    font-weight: 700;
    font-size: 40px;
    line-height: 52px;
    color: var(--company-green);
  }
  .company-name .line-two { display: block; padding-left: 36px; }
  .credential {
    position: absolute;
    top: 238px;
    left: 250px;
    font-family: 'Lato', sans-serif;
    font-size: 34px;
    color: var(--body-ink);
  }
  .coin-illustration {
    position: absolute;
    left: 40px;
    top: 170px;
    width: 190px;
    height: 260px;
    border-radius: 10px;
    background: radial-gradient(ellipse at 40% 45%, var(--coin-light) 0%, #e8b52c 55%, var(--coin-deep) 100%);
    opacity: 0.85;
  }
  .address-block {
    position: absolute;
    left: 430px;
    top: 370px;
    font-family: 'Lato', sans-serif;
    font-style: normal;
    font-size: 31px;
    line-height: 40px;
    color: var(--body-ink);
  }
  .address-row { display: flex; align-items: center; gap: 12px; }
  .contact-icon { width: 22px; height: 28px; flex: none; }
  .icon-spacer { width: 22px; flex: none; }
</style>
</head>
<body>
  <main class="canvas">
    <section class="business-card">
      <div class="advisor-name">Desmond Wick Harlow</div>

      <div class="coin-illustration" role="img" aria-label="Illustration of stacked gold coins with a golden upward arrow pointing right"></div>

      <h1 class="company-name">
        <span class="line-one">B. Rel K. Financial Consulting</span>
        <span class="line-two">&amp; Wealth Management</span>
      </h1>

      <p class="credential">Registered Investment Advisor</p>

      <address class="address-block">
        <div class="address-row">
          <svg class="contact-icon" viewBox="0 0 22 28" aria-hidden="true">
            <path d="M11 1C5.5 1 1.5 5 1.5 10.3 1.5 17 11 27 11 27s9.5-10 9.5-16.7C20.5 5 16.5 1 11 1z" fill="#222"/>
            <circle cx="11" cy="10.3" r="3.6" fill="#f9ee8c"/>
          </svg>
          <span>5172 Paseo Loma Verde Crest,</span>
        </div>
        <div class="address-row">
          <svg class="contact-icon" viewBox="0 0 22 28" aria-hidden="true">
            <path d="M5 4l4 0 2 6-3 2c1.2 3 3 5 6 6.3l2-3 6 2v4c0 1.4-1.2 2.4-2.6 2.2C10 22.5 3.5 16 2.8 6.6 2.7 5.2 3.6 4 5 4z" fill="#222"/>
          </svg>
          <span>San Diego, CA</span>
        </div>
        <div class="address-row">
          <span class="icon-spacer"></span>
          <span>92131-4817,</span>
        </div>
      </address>
    </section>
  </main>
</body>
</html>
```